Pelton|Marsh & Quillan business card contest

We need a logo for an upscale boutique diversified company involved in real estate, investments, cattle, and more. Our businesses DO NOT need to be reflected in the business card nor do we want them noted. This is our logo and colors and we love our logo and colors. Our logo looks best against a black background and we like to include the firm name in our logo usage. importantly, the names Pelton and Marsh are separated by | not / and we use an ampersand not the word and.
On the front of the card, we want to include:
company logo and name (Pelton|Marsh & Quillan)
on the back, we would definitely include:
address, email, cell #
logo and name (smaller size than front)

The variable will be location of individual name and title (mine for example is ) - whether on the front OR on the back. interested in variations from which to choose
Dr. Neil R. Whitcombe, CFA
Scientifique des Fusées Financières

we would like to use contemporary symbols for address, email address, cell # with an option for web site that we do not intend to use initially. we like two sided cards and believe this design should use four rounded corners with the standard size. we prefer thicker card stock and may look at metal.

```html
<!DOCTYPE html>
<html lang="en">
<head>
<meta charset="utf-8">
<title>Pelton|Marsh &amp; Quillan – Business Card</title>
<link rel="stylesheet" href="https://fonts.googleapis.com/css2?family=Roboto:wght@400;500;700&display=swap">
<style>
  :root {
    --page-bg: #efefef;
    --card-bg: #0d0d0d;
    --orange: #e8822a;
    --orange-deep: #c9561d;
    --grey-text: #8a8a8a;
    --grey-mark: #6b6b6b;
    --stripe-dark: #2a2a2a;
  }
  * { box-sizing: border-box; margin: 0; padding: 0; }
  html, body {
    width: 1200px; height: 1200px; overflow: hidden;
    background: var(--page-bg);
    font-family: "Roboto", Arial, sans-serif;
  }
  .card {
    position: absolute; left: 240px; width: 720px; height: 419px;
    background: var(--card-bg);
    border-radius: 10px;
    overflow: hidden;
  }
  .card--front { top: 142px; }
  .card--back  { top: 636px; }

  .brand {
    display: flex; align-items: center;
    color: var(--grey-mark); font-weight: 400; white-space: nowrap;
  }
  .brand__square { background: var(--orange); flex: none; }

  .card--front .brand {
    position: absolute; left: 0; right: 0; top: 180px;
    justify-content: center; gap: 18px; font-size: 36px;
  }
  .card--front .brand__square { width: 30px; height: 30px; }

  .card--back .brand {
    position: absolute; left: 27px; top: 112px;
    gap: 10px; font-size: 21px;
  }
  .card--back .brand__square { width: 18px; height: 18px; }

  .holder {
    position: absolute; right: 26px; top: 192px; text-align: right;
  }
  .holder__name {
    color: var(--orange); font-weight: 700; font-size: 24px; line-height: 30px;
  }
  .holder__title {
    color: var(--grey-text); font-size: 17px; line-height: 22px; margin-top: 2px;
  }
  .divider {
    position: absolute; left: 27px; right: 26px; top: 258px;
    height: 1px; background: var(--orange);
  }

  .contacts {
    position: absolute; left: 27px; top: 296px; list-style: none;
  }
  .contacts li {
    display: flex; align-items: center; gap: 9px;
    color: var(--grey-text); font-size: 17px; height: 26.5px;
  }
  .contacts svg { width: 16px; height: 16px; flex: none; }

  .address {
    position: absolute; right: 26px; top: 322px; text-align: right;
    color: var(--grey-text); font-size: 17px; line-height: 26.5px;
    font-style: normal;
  }

  .footer-band {
    position: absolute; left: 0; bottom: 0; width: 445px; height: 25px;
    background: linear-gradient(to bottom, var(--orange-deep), var(--orange));
  }
  .footer-stripes {
    position: absolute; left: 445px; right: 0; bottom: 0; height: 25px;
    background: linear-gradient(to right, var(--stripe-dark), var(--grey-mark));
  }
</style>
</head>
<body>

<section class="card card--front" aria-label="Card front">
  <div class="brand">
    <span class="brand__square"></span>
    <span class="brand__name">Pelton|Marsh &amp; Quillan</span>
  </div>
</section>

<section class="card card--back" aria-label="Card back">
  <div class="brand">
    <span class="brand__square"></span>
    <span class="brand__name">Pelton|Marsh &amp; Quillan</span>
  </div>

  <div class="holder">
    <p class="holder__name">Dr. Neil R. Whitcombe, CFA</p>
    <p class="holder__title">Scientifique des Fusées Financières</p>
  </div>

  <div class="divider"></div>

  <ul class="contacts">
    <li>
      <svg viewBox="0 0 24 24" aria-hidden="true"><path fill="var(--orange)" d="M6.6 10.8a15 15 0 0 0 6.6 6.6l2.2-2.2c.3-.3.7-.4 1-.2 1.1.4 2.3.6 3.6.6.6 0 1 .4 1 1V20c0 .6-.4 1-1 1A17 17 0 0 1 3 4c0-.6.4-1 1-1h3.5c.6 0 1 .4 1 1 0 1.3.2 2.5.6 3.6.1.3 0 .7-.2 1z"/></svg>
      <span>+0044-7712-5580</span>
    </li>
    <li>
      <svg viewBox="0 0 24 24" aria-hidden="true"><rect x="2" y="5" width="20" height="14" rx="1" fill="var(--orange)"/><path d="M3 6l9 7 9-7" fill="none" stroke="var(--card-bg)" stroke-width="1.6"/></svg>
      <span>office@peltonmarsh.co.uk</span>
    </li>
    <li>
      <svg viewBox="0 0 24 24" aria-hidden="true"><circle cx="12" cy="12" r="10" fill="var(--orange)"/><path d="M12 2c-3 3-3 17 0 20M12 2c3 3 3 17 0 20M2 12h20" fill="none" stroke="var(--card-bg)" stroke-width="1.4"/></svg>
      <span>www.peltonmarsh.co.uk</span>
    </li>
  </ul>

  <address class="address">
    P.O. Box: 456, Carrow Lane<br>
    212/ London, United Kingdom
  </address>

  <div class="footer-band"></div>
  <div class="footer-stripes" role="img" aria-label="Decorative vertical stripe pattern in grey"></div>
</section>

</body>
</html>
```